Webdesign für eine Softwarewarentwicklung und Consulting für das Gesundheitswesen
Zielgruppe
Softwarewarentwicklung und Consulting für das Gesundheitswesen. Unsere Zielgruppe sind Unternehmen und Organisationen im Bereich des Gesundheitswesen. Weiter informationen auf derzeitiger Homepage unter www.vmt-pflegeloesung.de.
Aufgabenstellung
Das Webdesign sollte deutlich moderner und kreativer wirken als unsere derzeitige Hompage. (Die bisherige Hompage wurde seinerzeit bei der Gründung 'auf die Schnelle' entwickelt.) Die neue Homapage sollte 'frisch' wirken und einem modernen Softwareunternehmen entsprechen.: Schlicht, modern und innovativ. Die Website sollte auch später gut auf Handy und Tablet darstellbar sein. Da wir derzeit wenig Inhalte auf unserer Homepage haben, wären wir auch für inhaltliche Vorschläge dankbar. Unsere Logofarben sollten sich auch im Design wiederfinden (der Rotton hat den Wert RGB: 227, 7, 19 #e30713 - der Blauton hat den Wert RGB: 30, 38, 74 1 #e264a).
Im Format bin ich unerfahren und würde dann für das spätere Umsetzen Adobe Photoshop vorschlagen.
Idealerweise sollte sich das Design später in einem gängigen CMS umsetzen lassen.
Gerne können Sie uns auch ein Komplettangebot auch zum Thema Umsetzung unterbreiten.
Grundsätzlich finde ich folgende Hompages ganz gut:
https://brelvuno.com/
https://www.kiesfeld.de/
https://www.plumvantic.com/de/
https://zirkanu.de/

```html
<!DOCTYPE html>
<html lang="de">
<head>
<meta charset="utf-8">
<title>VMT – Individuelle Software für das Gesundheitswesen</title>
<link href="https://fonts.googleapis.com/css2?family=IBM+Plex+Sans:wght@500;600;700&family=Open+Sans:wght@400;600;700&display=swap" rel="stylesheet">
<style>
:root{
  --red:#e30713;
  --navy:#1e264a;
  --ink:#1e264a;
  --text:#555a6e;
  --muted:#8a8ea0;
  --white:#ffffff;
  --line:#3a4266;
}
*{box-sizing:border-box;margin:0;padding:0}
html,body{width:1200px;height:4853px;overflow:hidden}
body{position:relative;background:var(--white);font-family:"Open Sans",sans-serif;color:var(--text)}
.abs{position:absolute}
h1,h2,h3{font-family:"IBM Plex Sans",sans-serif;color:var(--ink)}
.brand{font-family:"IBM Plex Sans",sans-serif;font-weight:700;letter-spacing:2px;color:var(--red)}
.decor{position:absolute;left:0;top:0;z-index:0}
.layer{position:relative;z-index:1}

.nav-logo{left:32px;top:20px;font-size:30px}
.nav-links{left:152px;top:30px;display:flex;gap:22px;font-size:9px;font-weight:700;letter-spacing:.5px;color:var(--navy)}
.nav-links span:first-child{font-weight:600}
.btn-contact{left:1098px;top:22px;width:72px;height:30px;border-radius:15px;background:var(--white);box-shadow:0 4px 14px rgba(30,38,74,.15);font-size:8px;font-weight:700;color:var(--navy);display:flex;align-items:center;justify-content:center;letter-spacing:.5px}

.side-mail{left:22px;top:370px;transform:rotate(-90deg);transform-origin:left top;font-size:9px;color:var(--navy);white-space:nowrap}
.side-scroll{left:24px;top:568px;transform:rotate(-90deg);transform-origin:left top;font-size:8px;color:var(--navy)}
.side-line{left:29px;top:560px;width:1px;height:48px;background:var(--navy)}
.side-dot{left:26px;top:566px;width:6px;height:6px;border-radius:50%;background:var(--navy)}

.hero-title{left:245px;top:96px;font-size:34px;line-height:1.18;font-weight:700;width:520px}
.hero-sub{left:250px;top:200px;font-size:12px;line-height:1.6;width:460px;color:var(--muted)}
.hero-img{left:529px;top:273px;width:428px;height:239px;background:linear-gradient(180deg,#c5c9d8 0%,#9aa0b8 45%,#f0707a 70%,#e8505c 100%)}
.hero-mark{left:590px;top:340px;font-size:96px;color:var(--white);letter-spacing:8px}

.intro-box{left:241px;top:588px;width:426px;height:314px;background:var(--navy);overflow:hidden;padding:38px 38px}
.intro-box h2{color:var(--white);font-size:26px;font-weight:700;margin-bottom:22px;position:relative}
.intro-box p{color:#e2e4ee;font-size:11.5px;line-height:1.65;position:relative}

.talk-title{left:244px;top:978px;font-size:29px;font-weight:600}
.talk-text{left:244px;top:1034px;width:292px;font-size:11.5px;line-height:1.64}
.btn-red{background:var(--red);color:var(--white);font-size:8.5px;font-weight:700;letter-spacing:.5px;border-radius:22px;display:flex;align-items:center;justify-content:center;box-shadow:0 8px 18px rgba(227,7,19,.3)}
.talk-btn{left:244px;top:1275px;width:105px;height:42px}
.photo{box-shadow:0 10px 30px rgba(30,38,74,.25)}
.ph-code{left:784px;top:918px;width:160px;height:156px;background:linear-gradient(135deg,#1d2a44,#2f4a6e 60%,#1a2336)}
.ph-team{left:563px;top:1021px;width:253px;height:215px;background:linear-gradient(180deg,#eef2f6,#a8c8de 55%,#4f7fb4)}
.ph-screen{left:744px;top:1157px;width:245px;height:166px;background:linear-gradient(135deg,#2a2e36,#6a7584 50%,#c9a27e)}

.sol-title{left:350px;top:1393px;font-size:29px;font-weight:600}
.card{width:206px;height:209px;padding:0 24px;display:flex;flex-direction:column;justify-content:center;box-shadow:0 14px 30px rgba(30,38,74,.25)}
.card h3{color:var(--white);font-size:14px;font-weight:700;margin-bottom:10px}
.card p{color:#eef0f6;font-size:9.5px;line-height:1.75}
.card.navy{background:var(--navy)}
.card.red{background:var(--red)}

.review-img{width:317px;height:441px}
.review-label{font-size:9px;color:var(--muted);transform:rotate(-90deg);transform-origin:left top;white-space:nowrap}
.review-title{font-size:49px;line-height:1;font-weight:700}
.review-title.red{color:var(--red)}
.review-text{font-size:10px;line-height:1.7;width:215px}
.rv1{left:260px;top:2110px;background:linear-gradient(180deg,#e9c9cf,#f2dfe2 40%,#d9a483 75%,#f3e6e4)}
.rv2{left:405px;top:2626px;background:linear-gradient(160deg,#5e6680,#8890aa 45%,#c4c7d4 80%,#7a819a)}
.rv3{left:260px;top:3142px;background:linear-gradient(170deg,#f3c8cf,#e8a5b0 50%,#f1d6d9)}

.clients{left:121px;top:3653px;width:1079px;height:484px;background:var(--navy)}
.clients-title{left:160px;top:3720px;font-size:27px;font-weight:600;color:var(--white);z-index:2}
.client-cell{width:254px;height:119px;border:1px solid var(--line);display:flex;align-items:center;justify-content:center;gap:6px;color:#8a90ac;font-family:"IBM Plex Sans",sans-serif;font-weight:600;font-size:15px}
.client-cell i{width:8px;height:8px;border-radius:50%;background:#8a90ac;display:block}

.cta{left:207px;top:4215px;width:805px;height:220px;background:var(--white);box-shadow:0 16px 40px rgba(30,38,74,.1)}
.cta h2{position:absolute;left:50px;top:46px;font-size:30px;line-height:1.3;font-weight:600}
.cta p{position:absolute;left:50px;top:144px;width:490px;font-size:12px;line-height:1.55}
.cta-btn{left:782px;top:4303px;width:177px;height:43px}

.ft-photo{left:480px;top:4501px;width:720px;height:352px;background:linear-gradient(120deg,#1e3f8a,#3a78c8 35%,#0d1a3a 60%,#6b4a3a 85%,#2a1f1e)}
.ft-box{left:0;top:4573px;width:720px;height:213px;background:var(--navy)}
.ft-claim{left:53px;top:4625px;font-size:14px;line-height:1.35;color:var(--white)}
.ft-logo{left:620px;top:4618px;font-size:24px;color:var(--white)}
.ft-col{font-size:9px;line-height:1.9;color:#d8dbe8}
.ft-bar{left:0;top:4786px;width:720px;height:67px;background:var(--red);display:flex;align-items:center;justify-content:center;color:var(--white);font-size:9px}
</style>
</head>
<body>

<svg class="decor" width="1200" height="4853" aria-hidden="true">
  <path d="M60 980 C200 860 560 900 760 960 C980 1020 1080 1180 980 1330 C860 1480 420 1470 200 1380 C40 1310 -20 1100 60 980Z" fill="#f8f4fb"/>
  <path d="M420 1480 C600 1380 980 1430 1030 1620 C1080 1820 940 2040 700 2040 C460 2040 300 1900 300 1740 C300 1620 330 1540 420 1480Z" fill="#f9f6fb"/>
  <path d="M720 2180 C900 1980 1220 2020 1200 2200 L1200 3150 C1100 3260 820 3180 740 2950 C660 2720 600 2340 720 2180Z" fill="#f8f4fb"/>
  <path d="M0 2900 C160 2860 360 3000 360 3200 C360 3420 160 3520 0 3480Z" fill="#f9f6fb"/>
  <circle cx="596" cy="16" r="2" fill="#e30713"/>
  <circle cx="633" cy="56" r="2" fill="#e30713"/>
  <circle cx="228" cy="85" r="2" fill="#1e264a"/>
  <circle cx="865" cy="145" r="2" fill="#4a56a0"/>
  <circle cx="432" cy="247" r="2" fill="#1e264a"/>
</svg>

<div class="layer">
  <div class="abs brand nav-logo">VMT</div>
  <nav class="abs nav-links"><span>Home</span><span>PRODUKTE</span><span>ÜBER UNS</span><span>JOBANGEBOTE</span></nav>
  <div class="abs btn-contact">KONTAKT</div>

  <div class="abs side-mail">info@vmt-pflegeloesung.de</div>
  <div class="abs side-scroll">scroll</div>
  <div class="abs side-line"></div>
  <div class="abs side-dot"></div>

  <h1 class="abs hero-title">Individuelle Software für das Gesundheitswesen</h1>
  <p class="abs hero-sub">Wir beschleunigen technologische Innovation und gestalten die Art der Gesundheitsversorgung von Patienten neu Lesen Sie mehr auf neuwelle-praxis.de</p>
  <div class="abs hero-img" role="img" aria-label="Foto: Ärzteteam bei der Besprechung am Laptop, blau-rot getönt"></div>
  <div class="abs brand hero-mark">VMT</div>

  <section class="abs intro-box">
    <svg class="abs" style="left:0;top:0" width="426" height="314" aria-hidden="true">
      <path d="M0 40 C120 0 300 10 426 60 L426 0 L0 0Z" fill="#232c55"/>
      <path d="M0 280 C140 230 300 240 426 270 L426 314 L0 314Z" fill="#273160"/>
    </svg>
    <h2>Erfolgsorientiert</h2>
    <p>Die VMT Softwareentwicklung für das Gesundheitswesen AG ( VMT ) mit ihrer Betriebsstätte in Velbrück, ist der kompetente Dienstleister für zukunftsorientierte Unternehmen im Gesundheitswesen. Mit einem erfahrenen Team und höchster Fachkompetenz bieten wir Lösungen, die Ihr Unternehmen im digitalen Wandel des Gesundheitswesens unterstützen. Kontaktieren Sie uns gerne – wir freuen uns auf Ihren Anruf</p>
  </section>

  <h2 class="abs talk-title">Lass uns reden</h2>
  <p class="abs talk-text">VMT kann auf eine langjährige Erfahrung in der Bereitstellung von IT-Dienstleistungen für Kunden aus dem Gesundheitswesen zurückblicken. Unsere Softwarelösungen für das Gesundheitswesen zielen darauf ab, Innovationen und Digitalisierungsprozesse in Krankenhäusern, Kliniken, ländlichen medizinischen Zentren, Blutverarbeitungsunternehmen, Einzelpraxen und Medizintechnikunternehmen zu beschleunigen. Als Unternehmen für Softwareentwicklung im Gesundheitswesen liefern wir Lösungen, die so präzise und akkurat arbeiten wie Chirurgen.</p>
  <div class="abs btn-red talk-btn">ÜBER UNS</div>
  <div class="abs photo ph-code" role="img" aria-label="Foto: Programmcode auf einem Bildschirm"></div>
  <div class="abs photo ph-team" role="img" aria-label="Foto: Gruppe von Ärzten und Pflegekräften"></div>
  <div class="abs photo ph-screen" role="img" aria-label="Foto: Hand zeigt auf Software-Oberfläche am Monitor"></div>

  <h2 class="abs sol-title">Digitale Zukunftslösungen</h2>
  <div class="abs card red" style="left:497px;top:1468px"><h3>Digitalisierung</h3><p>Muster kurze Beschreibung Lorem ipsum dolor sit amet, consetetur sadipscing elitr, sed diam nonumy eirmod tempor invidunt ut labore et dolore magna rebum...</p></div>
  <div class="abs card navy" style="left:254px;top:1562px"><h3>Prozessoptimierung</h3><p>Muster kurze Beschreibung Lorem ipsum dolor sit amet, consetetur sadipscing elitr, sed diam nonumy eirmod tempor invidunt ut labore et dolore magna rebum...</p></div>
  <div class="abs card navy" style="left:740px;top:1626px"><h3>Onlineanwendung</h3><p>Muster kurze Beschreibung Lorem ipsum dolor sit amet, consetetur sadipscing elitr, sed diam nonumy eirmod tempor invidunt ut labore et dolore magna rebum...</p></div>
  <div class="abs card navy" style="left:497px;top:1698px"><h3>Consulting</h3><p>Muster kurze Beschreibung Lorem ipsum dolor sit amet, consetetur sadipscing elitr, sed diam nonumy eirmod tempor invidunt ut labore et dolore magna rebum...</p></div>
  <div class="abs card red" style="left:254px;top:1792px"><h3>eRezept / E-Health</h3><p>Muster kurze Beschreibung Lorem ipsum dolor sit amet, consetetur sadipscing elitr, sed diam nonumy eirmod tempor invidunt ut labore et dolore magna rebum...</p></div>
  <div class="abs card red" style="left:740px;top:1856px"><h3>Projektmanagement</h3><p>Muster kurze Beschreibung Lorem ipsum dolor sit amet, consetetur sadipscing elitr, sed diam nonumy eirmod tempor invidunt ut labore et dolore magna rebum...</p></div>

  <div class="abs review-img rv1" role="img" aria-label="Foto: heller Empfangsbereich einer Klinik"></div>
  <div class="abs review-label" style="left:244px;top:2360px">Muster Klinikum</div>
  <h2 class="abs review-title" style="left:539px;top:2246px">Muster<br>Rezension</h2>
  <p class="abs review-text" style="left:587px;top:2352px">Muster Text Lorem ipsum dolor sit amet, consectetur adipiscing elit. Ut elit tellus, luctus nec ullamcorper mattis, pulvinar dapibus leo.</p>

  <div class="abs review-img rv2" role="img" aria-label="Foto: Arzt arbeitet an einem Computerterminal"></div>
  <div class="abs review-label" style="left:389px;top:2876px">Muster Klinikum</div>
  <h2 class="abs review-title red" style="left:684px;top:2762px">Muster<br>Rezension</h2>
  <p class="abs review-text" style="left:732px;top:2868px">Muster Text Lorem ipsum dolor sit amet, consectetur adipiscing elit. Ut elit tellus, luctus nec ullamcorper mattis, pulvinar dapibus leo.</p>

  <div class="abs review-img rv3" role="img" aria-label="Foto: zwei Pflegekräfte am Computer, rosa getönt"></div>
  <div class="abs review-label" style="left:244px;top:3392px">Muster Klinikum</div>
  <h2 class="abs review-title" style="left:539px;top:3278px">Muster<br>Rezension</h2>
  <p class="abs review-text" style="left:587px;top:3384px">Muster Text Lorem ipsum dolor sit amet, consectetur adipiscing elit. Ut elit tellus, luctus nec ullamcorper mattis, pulvinar dapibus leo.</p>

  <section class="abs clients"></section>
  <h2 class="abs clients-title">Kunden</h2>
  <div class="abs client-cell" style="left:405px;top:3715px"><i></i>norvale</div>
  <div class="abs client-cell" style="left:659px;top:3715px">quintor</div>
  <div class="abs client-cell" style="left:151px;top:3834px">velaro</div>
  <div class="abs client-cell" style="left:405px;top:3834px">brisko</div>
  <div class="abs client-cell" style="left:659px;top:3834px">tamora</div>
  <div class="abs client-cell" style="left:151px;top:3953px"><i></i>norvale</div>
  <div class="abs client-cell" style="left:405px;top:3953px"><i></i>lunex</div>
  <div class="abs client-cell" style="left:659px;top:3953px"><i></i>norvale</div>
  <div class="abs client-cell" style="left:913px;top:3953px">velaro</div>

  <section class="abs cta">
    <h2>Bereit für eine<br>Zusammenarbeit?</h2>
    <p>Muster Text Lorem ipsum dolor sit amet, consetetur sadipscing elitr, sed diam nonumy eirmod tempor invidunt ut labore et dolore magna aliquyam erat, sed diam voluptua.</p>
  </section>
  <div class="abs btn-red cta-btn">KONTAKT AUFNEHMEN</div>

  <div class="abs ft-photo" role="img" aria-label="Foto: moderne Glasfassade eines Bürogebäudes"></div>
  <footer class="abs ft-box"></footer>
  <p class="abs ft-claim">Lassen Sie uns gemeinsam etwas<br>Großartiges entwickeln</p>
  <div class="abs brand ft-logo">VMT</div>
  <p class="abs ft-col" style="left:53px;top:4700px">VMT AG<br>Lindenweg 17<br>40210 Velbrück</p>
  <p class="abs ft-col" style="left:213px;top:4700px">Tel.: +49 21 00 / 5 55 01 - 00<br>Mail: info@vmt-pflegeloesung.de<br>Web.: vmt-pflegeloesung.de</p>
  <p class="abs ft-col" style="left:624px;top:4700px;text-align:right">Datenschutz<br>Impressum</p>
  <div class="abs ft-bar">© VMT – Softwareentwicklung für das Gesundheitswesen</div>
</div>

</body>
</html>
```